Brookfarrow Osteopathy and dry needling business card

Business card for Brookfarrow Osteopathy and Dry Needling.

Industry/Entity Type

Health

Contact Information for Business Card

I do not have a phone number yet. I also do not have an email address yet. The physical address is: 48 Lower Crane Street Brookfarrow The website is: www.brookfarrowosteosteopathy.example My details are: Dr Martin Pellowe, Osteopath (B.Clin.Sci (Ost) M.Ost BSC ECON (Hons)

Colors
0094D4
00A9DD
6FCCEA
C7EBF8
E9F6FB

Requirements
Must have
• logo on the back
Nice to have
• Maybe a space for me to write an appointment time and date on the card.

```html
<!DOCTYPE html>
<html lang="en">
<head>
<meta charset="utf-8">
<title>Brookfarrow Osteopathy and Dry Needling – Business Card</title>
<link rel="stylesheet" href="https://fonts.googleapis.com/css2?family=Montserrat:wght@400;500;700&display=swap">
<style>
  :root {
    --brand-blue: #0094D4;
    --brand-cyan: #00A9DD;
    --brand-sky: #6FCCEA;
    --brand-mist: #C7EBF8;
    --brand-ice: #E9F6FB;
    --paper: #FFFFFF;
    --backdrop: #2A2A2E;
  }
  * { box-sizing: border-box; margin: 0; padding: 0; }
  html, body { width: 1200px; height: 947px; overflow: hidden; }
  body {
    background: var(--backdrop);
    font-family: "Montserrat", sans-serif;
    color: var(--paper);
    position: relative;
  }
  .card {
    position: absolute;
    left: 280px;
    width: 640px;
    height: 400px;
    border-radius: 22px;
    background: var(--brand-blue);
    overflow: hidden;
  }
  .card--back { top: 48px; }
  .card--front { top: 499px; }

  /* Back */
  .brand-mark {
    position: absolute;
    top: 50%; left: 50%;
    transform: translate(-50%, -50%);
    display: flex; align-items: center; gap: 16px;
  }
  .brand-mark__dot {
    width: 34px; height: 34px; border-radius: 50%;
    border: 3px solid var(--paper);
    flex: none;
  }
  .brand-mark__name {
    font-weight: 500; font-size: 26px; letter-spacing: 2px;
    text-transform: uppercase; line-height: 1.25;
  }
  .brand-mark__name span { display: block; font-size: 15px; letter-spacing: 3px; }

  /* Front */
  .spine-panel { position: absolute; inset: 0; }
  .contact {
    position: absolute; left: 40px; top: 108px;
  }
  .contact__name { font-weight: 700; font-size: 30px; line-height: 1.1; }
  .contact__role { font-size: 14px; line-height: 1.35; margin-top: 6px; }
  .contact__address { font-size: 14px; margin-top: 20px; }
  .contact__web { font-size: 14px; margin-top: 10px; }
  .contact__web strong { font-weight: 700; }

  .appointment {
    position: absolute; right: 40px; top: 32px; width: 230px;
    font-size: 15px;
  }
  .appointment__row { display: flex; align-items: flex-end; gap: 6px; margin-bottom: 10px; }
  .appointment__line { flex: 1; border-bottom: 1px dashed var(--paper); height: 14px; }
  .appointment__days { display: flex; gap: 7px; margin-top: 4px; }
  .appointment__day {
    width: 24px; height: 24px; border-radius: 50%;
    border: 1.5px solid var(--paper);
    font-size: 11px; font-weight: 500;
    display: flex; align-items: center; justify-content: center;
  }
  .brand-mark--small {
    position: absolute; right: 40px; top: 128px;
    display: flex; align-items: center; gap: 8px;
  }
  .brand-mark--small .brand-mark__dot { width: 16px; height: 16px; border-width: 2px; }
  .brand-mark--small .brand-mark__name { font-size: 11px; letter-spacing: 1px; }
  .brand-mark--small .brand-mark__name span { font-size: 8px; letter-spacing: 1.5px; }
</style>
</head>
<body>

<section class="card card--back" aria-label="Card back">
  <div class="brand-mark">
    <div class="brand-mark__dot"></div>
    <div class="brand-mark__name">Brookfarrow Osteopathy<span>&amp; Dry Needling</span></div>
  </div>
</section>

<section class="card card--front" aria-label="Card front">
  <svg class="spine-panel" viewBox="0 0 640 400" preserveAspectRatio="none">
    <path d="M250 400 C290 330 350 300 450 285 C550 270 605 210 640 160 L640 400 Z" fill="var(--paper)"/>
    <path role="img" aria-label="Spine illustration along the curve"
          d="M250 400 C290 330 350 300 450 285 C550 270 605 210 640 160 L640 192 C606 242 555 296 456 310 C365 323 310 350 282 400 Z"
          fill="var(--brand-blue)"/>
  </svg>

  <div class="appointment">
    <div class="appointment__row">Date:<span class="appointment__line"></span></div>
    <div class="appointment__row">Time:<span class="appointment__line"></span>am/pm</div>
    <div class="appointment__days">
      <span class="appointment__day">M</span><span class="appointment__day">T</span>
      <span class="appointment__day">W</span><span class="appointment__day">T</span>
      <span class="appointment__day">F</span><span class="appointment__day">S</span>
    </div>
  </div>

  <div class="brand-mark--small">
    <div class="brand-mark__dot"></div>
    <div class="brand-mark__name">Brookfarrow Osteopathy<span>&amp; Dry Needling</span></div>
  </div>

  <div class="contact">
    <h1 class="contact__name">Dr Martin Pellowe</h1>
    <p class="contact__role">Osteopath (B.Clin.Sci (Ost)<br>M.Ost BSC ECON (Hons)</p>
    <p class="contact__address">48 Lower Crane Street Brookfarrow</p>
    <p class="contact__web">www.<strong>brookfarrowosteosteopathy</strong>.example</p>
  </div>
</section>

</body>
</html>
```